Gift card design to reflect the theme from our overhead business sign

We need a gift card that aligns with our colors used for the sign. Since I am not sure what you're able to do with the limited space, if you think you can create a miniature version of the sign and add the words "Gift Card" to it. I'd like to see it. I have also uploaded the original logo we use as an other variable to use in place the horizontal one on the sign. That might be alright too. Give me a few options to consider.

Then for the back of the card there may be some legal requirements for the wording. I'll get back to you on that. First, let's focus on the design.

Also, i am sending the requirements for "Tormix" who will be the processor for the card. I will be doing custom cards so pay attention to page 4.

After the gift card, I will sending you the front of the store image with the sign in place, so you can come up with some ideas for a simple window design to go across all the windows.

How fast can you get back to me? Unlike the sign, I'm sort of in a time crunch.

Oh, one other thing, I want to change the pink in our current logo to the pink you used in the sign. So if you use our standard logo, please change the pink to the on you used for the sign.

```html
<!DOCTYPE html>
<html lang="en">
<head>
<meta charset="utf-8">
<title>Maple Crumb Bakery – Gift Card Options</title>
<link rel="stylesheet" href="https://fonts.googleapis.com/css2?family=Fredoka:wght@600&family=Arimo:wght@700&display=swap">
<style>
  :root {
    --pink: #EC3995;
    --pink-deep: #B1266F;
    --orange: #F48A33;
    --lime: #AFD34B;
    --white: #FFFFFF;
    --label-grey: #939598;
    --page: #FFFFFF;
  }
  * { margin: 0; padding: 0; box-sizing: border-box; }
  html, body {
    width: 1200px; height: 900px; overflow: hidden;
    background: var(--page);
  }
  .sheet { position: relative; width: 1200px; height: 900px; }

  .option-number {
    position: absolute;
    font-family: "Arimo", Arial, sans-serif;
    font-weight: 700;
    font-size: 40px;
    color: var(--label-grey);
    line-height: 1;
  }

  .card {
    position: absolute;
    width: 390px; height: 256px;
    border-radius: 14px;
    overflow: hidden;
    font-family: "Fredoka", sans-serif;
    font-weight: 600;
  }
  .card--pink { background: var(--pink); }
  .card--lime { background: var(--lime); }
  .card--framed { background: var(--lime); }

  .stripe { position: absolute; left: 0; width: 100%; height: 18px; }
  .stripe--orange { top: 167px; background: var(--orange); }
  .stripe--lime { top: 200px; background: var(--lime); }

  .frame-orange {
    position: absolute; inset: 14px;
    background: var(--orange); border-radius: 6px;
  }
  .frame-pink {
    position: absolute; inset: 28px;
    background: var(--pink); border-radius: 4px;
  }

  .brand-name {
    position: absolute; left: 0; width: 100%;
    text-align: center;
    color: var(--white);
    line-height: 1;
    white-space: nowrap;
  }
  .brand-name--inline { font-size: 35px; }
  .brand-name--stacked { font-size: 42px; line-height: 0.95; }
  .card--lime .brand-name { color: var(--pink); }

  .tagline {
    position: absolute;
    color: var(--white);
    font-size: 20px;
    text-shadow: 2px 2px 0 var(--pink-deep);
    line-height: 1;
    white-space: nowrap;
  }

  .gift-label {
    position: absolute;
    color: var(--white);
    font-size: 40px;
    line-height: 1;
    text-shadow:
      -1px -1px 0 var(--pink-deep), 1px -1px 0 var(--pink-deep),
      -1px 1px 0 var(--pink-deep), 1px 1px 0 var(--pink-deep),
      4px 4px 0 var(--pink-deep);
    white-space: nowrap;
  }
  .gift-label--small { font-size: 34px; }
  .card--lime .gift-label { text-shadow: none; font-size: 44px; }
</style>
</head>
<body>
<main class="sheet">

  <span class="option-number" style="left:80px; top:38px;">1.</span>
  <section class="card card--pink" style="left:135px; top:34px;">
    <div class="brand-name brand-name--inline" style="top:48px;">Maple Crumb Bakery</div>
    <div class="tagline" style="left:168px; top:90px;">fresh bakes daily</div>
    <div class="stripe stripe--orange"></div>
    <div class="stripe stripe--lime"></div>
    <div class="gift-label" style="right:30px; top:168px;">Gift Card</div>
  </section>

  <span class="option-number" style="left:630px; top:38px;">2.</span>
  <section class="card card--pink" style="left:683px; top:34px;">
    <div class="brand-name brand-name--stacked" style="top:46px;">Maple Crumb<br>Bakery</div>
    <div class="stripe stripe--orange"></div>
    <div class="stripe stripe--lime"></div>
    <div class="gift-label" style="right:30px; top:168px;">Gift Card</div>
  </section>

  <span class="option-number" style="left:80px; top:330px;">3.</span>
  <section class="card card--framed" style="left:135px; top:325px;">
    <div class="frame-orange"></div>
    <div class="frame-pink"></div>
    <div class="brand-name brand-name--inline" style="top:90px; font-size:32px;">Maple Crumb Bakery</div>
    <div class="gift-label gift-label--small" style="right:62px; top:140px;">Gift Card</div>
  </section>

  <span class="option-number" style="left:630px; top:330px;">4.</span>
  <section class="card card--framed" style="left:683px; top:325px;">
    <div class="frame-orange"></div>
    <div class="frame-pink"></div>
    <div class="brand-name brand-name--stacked" style="top:52px; font-size:38px;">Maple Crumb<br>Bakery</div>
    <div class="gift-label gift-label--small" style="right:66px; top:174px;">Gift Card</div>
  </section>

  <span class="option-number" style="left:355px; top:622px;">5.</span>
  <section class="card card--lime" style="left:407px; top:615px;">
    <div class="brand-name brand-name--stacked" style="top:48px;">Maple Crumb<br>Bakery</div>
    <div class="gift-label" style="right:34px; top:192px;">Gift Card</div>
  </section>

</main>
</body>
</html>
```